Corsets, Cups and Commerce needs a book cover

I've been in lingerie business for 12 years, we own 5 x Lingerie stores. This is my story aimed at women in business or women who want to start a business. Essentially its a business book but also offers bra fitting advice. Although the book cover can be a bit cheeky it also needs to be tasteful. I do not have a colour in mind I just don't like it too girly. I like strong and bold with a feminine touch. The title needs to catch peoples attention when surrounded by so many other books. It needs to have some sort of image or texture. That could be a lace background texture. I like the idea of a bra hanging off the letters or some kind of image of a bra but a beautiful lacy bra. I would like the cover to be more beautiful than tacky even though it has the word 'boobs'.
Updates

Hi everyone, some great designs so far. Many of you have made a bra part of the 'Boobs' word. I thought this could work but it doesn't as it covers up the word 'Boobs' too much and I feel this word will catch peoples attention. If any of you would like to revise please feel free. thankyou Delphine.

Target Market(s)

Women in business or women wanting to start a business.

Industry/Entity Type

Retail

Logo Text

Corsets, Cups and Commerce

Font styles to use
Serif
Sans Serif

Colors

Designer to choose colors to be used in the design.

Requirements
Must have
• Title: Corsets, Cups and Commerce (you could replace 'and' with '&' if it works better.
• Tagline: Steady Lessons for Women in Trade
• Author: Delphine Karsby
Nice to have
• An image of a bra, maybe in a playful way. It could hang off the letters or maybe the letters could look like a bra, but I'm concerned it may look tacky that way. Somehow incorporate a picture of a bra preferably as part of the title.
• I don't have images for you, you have the freedom to choose.
Should not have
• Although this book has boobs and bras in the title it must not be tacky or sexual. It is a business book.
• I do not like it to look too girly, probably not script unless its subtle.

```html
<!DOCTYPE html>
<html lang="en">
<head>
<meta charset="utf-8">
<title>Corsets, Cups and Commerce — Book Cover</title>
<link href="https://fonts.googleapis.com/css2?family=Montserrat:wght@400;700;800&family=Roboto+Condensed:wght@500&display=swap" rel="stylesheet">
<style>
  :root {
    --backdrop: #dcdcda;
    --paper: #fbfbfb;
    --lace: #ececec;
    --lace-soft: #f4f4f4;
    --pink: #ee98c8;
    --pink-deep: #e07cb4;
    --ink: #3c3c3c;
    --rule: #1e1e1e;
  }
  html, body {
    margin: 0;
    padding: 0;
    width: 1200px;
    height: 1200px;
    overflow: hidden;
    background: var(--backdrop);
  }
  .canvas {
    position: relative;
    width: 1200px;
    height: 1200px;
  }
  .cover {
    position: absolute;
    left: 200px;
    top: 0;
    width: 800px;
    height: 1200px;
    background: var(--paper);
    overflow: hidden;
  }
  .lace-frame {
    position: absolute;
    inset: 0;
    background:
      linear-gradient(to bottom, var(--lace) 0, var(--lace-soft) 80px, transparent 80px),
      linear-gradient(to top, var(--lace) 0, var(--lace-soft) 90px, transparent 90px),
      linear-gradient(to right, var(--lace) 0, var(--lace-soft) 50px, transparent 50px),
      linear-gradient(to left, var(--lace) 0, var(--lace-soft) 50px, transparent 50px);
  }
  .bra-image {
    position: absolute;
    left: 255px;
    top: 110px;
    width: 220px;
    height: 72px;
    border-radius: 40px 40px 14px 14px;
    background: linear-gradient(to bottom, var(--pink) 0%, var(--pink-deep) 100%);
  }
  .title {
    position: absolute;
    left: 0;
    top: 0;
  }
  .title text {
    font-family: "Montserrat", sans-serif;
    font-weight: 800;
  }
  .title .accent { fill: var(--pink); }
  .title .dark { fill: var(--ink); font-weight: 700; }
  .divider {
    position: absolute;
    left: 60px;
    width: 670px;
    height: 90px;
  }
  .divider-top { top: 582px; }
  .divider-bottom { top: 860px; }
  .flourish {
    position: absolute;
    top: 10px;
    width: 250px;
    height: 70px;
    background: var(--lace-soft);
  }
  .flourish-left { left: 0; }
  .flourish-right { right: 0; }
  .divider svg {
    position: absolute;
    left: 0;
    top: 0;
  }
  .tagline {
    position: absolute;
    left: 0;
    top: 700px;
    width: 800px;
    margin: 0;
    text-align: center;
    font-family: "Roboto Condensed", sans-serif;
    font-weight: 500;
    font-size: 60px;
    line-height: 72px;
    color: var(--ink);
    text-transform: uppercase;
  }
  .author-band {
    position: absolute;
    left: 0;
    top: 1047px;
    width: 800px;
    height: 57px;
    background: var(--pink);
    display: flex;
    align-items: center;
    justify-content: center;
    font-family: "Montserrat", sans-serif;
    font-weight: 400;
    font-size: 25px;
    letter-spacing: 1px;
    color: #222;
    text-transform: uppercase;
  }
</style>
</head>
<body>
<main class="canvas">
  <section class="cover">
    <div class="lace-frame" role="img" aria-label="Soft grey lace texture framing the cover edges"></div>

    <div class="bra-image" role="img" aria-label="Pink lace balconette bra hanging above the title"></div>

    <svg class="title" width="800" height="500" viewBox="0 0 800 500" aria-label="Corsets, Cups and Commerce">
      <text class="accent" x="140" y="272" font-size="118" textLength="525" lengthAdjust="spacingAndGlyphs">CORSETS,</text>
      <text class="dark" x="140" y="373" font-size="96" textLength="520" lengthAdjust="spacingAndGlyphs">CUPS AND</text>
      <text class="accent" x="143" y="472" font-size="98" textLength="520" lengthAdjust="spacingAndGlyphs">COMMERCE</text>
    </svg>

    <div class="divider divider-top">
      <div class="flourish flourish-left" role="img" aria-label="Black leafy scroll ornament"></div>
      <div class="flourish flourish-right" role="img" aria-label="Black leafy scroll ornament"></div>
      <svg width="670" height="90" viewBox="0 0 670 90">
        <line x1="260" y1="45" x2="415" y2="45" stroke="var(--rule)" stroke-width="2.5"/>
        <circle cx="260" cy="45" r="6" fill="var(--rule)"/>
        <circle cx="415" cy="45" r="6" fill="var(--rule)"/>
      </svg>
    </div>

    <p class="tagline">Steady Lessons for<br>Women in Trade</p>

    <div class="divider divider-bottom">
      <div class="flourish flourish-left" role="img" aria-label="Black leafy scroll ornament"></div>
      <div class="flourish flourish-right" role="img" aria-label="Black leafy scroll ornament"></div>
      <svg width="670" height="90" viewBox="0 0 670 90">
        <line x1="260" y1="44" x2="415" y2="44" stroke="var(--rule)" stroke-width="2.5"/>
        <circle cx="260" cy="44" r="6" fill="var(--rule)"/>
        <circle cx="415" cy="44" r="6" fill="var(--rule)"/>
      </svg>
    </div>

    <div class="author-band">Author: Delphine Karsby</div>
  </section>
</main>
</body>
</html>
```